UI Improvement for FlorQuay app

We are looking for a talented UI/UX designer to REFINE and enhance the visual design of our mobile application, FlorQuay. The app is fully functional, but we need a designer to improve its aesthetics by specifying design elements such as fonts, colors, spacing, and component styles.
Your task will be to analyze the CURRENT UI and provide detailed design specifications that will make the app more visually appealing, modern, and user-friendly.
TODO:
Review the existing FlorQuay app design (see attachments) and identify areas for visual improvement.
Provide a detailed UI style guide, including:
Typography (font choices, sizes, and weights)
Color palette (primary, secondary, and accent colors)
Component styling (buttons, forms, icons, and interactive elements)
Spacing and layout guidelines (margins, paddings, and alignment)
Ensure the design remains clean, modern, and professional while maintaining usability and accessibility.
Provide design mockups or visual examples (if possible) to illustrate the proposed changes.
Deliverables:
A UI Style Guide (PDF or Figma file) with specifications on fonts, colors, spacing, and UI components.
Optionally, before/after mockups or examples demonstrating the improvements.
Ideal Designer:
Strong experience in mobile UI/UX design.
Understanding of modern design trends and best practices.
Ability to communicate design choices clearly for easy developer implementation.
I have attached 7 images showcasing the main UI screens used in the FlorQuay app. These screens need visual enhancements to improve their overall look and user experience.
The images represent the current design in three key modes:
LIST Mode – Displays data in a structured list format.
READ Mode – Shows detailed information when a user selects an item.
ADD/EDIT Mode – Allows users to input or modify information.
Additionally, there is a ‘MORE’ page, which serves as a menu listing other features of the application.
Task Objective:
Please refine and improve these UIs to create a more modern, visually appealing, and user-friendly experience. Focus on typography, colors, spacing, and component styling to ensure a cohesive and polished design.
Look and feel
Each slider illustrates characteristics of the customer's brand and the style your logo design should communicate.

```html
<!DOCTYPE html>
<html lang="en">
<head>
<meta charset="utf-8">
<title>FlorQuay app screens</title>
<link href="https://fonts.googleapis.com/css2?family=Inter:wght@400;500;600;700&family=Outfit:wght@600&display=swap" rel="stylesheet">
<style>
:root{
  --ink:#1d2230;--muted:#9aa1ad;--line:#e3e6ec;--bg:#f5f6fa;--card:#fff;
  --blue:#2a64c5;--cyan:#1fa9cf;--teal:#20b39c;--plus:#2bb6de;
  --yellow:#fbf9e6;--yellowbar:#e9e08a;--sky:#e6f4fb;--skybar:#8fd0ea;
  --mint:#e2f6f0;--mintbar:#6ccfb4;--tabgray:#b3b8c2;
}
*{box-sizing:border-box;margin:0;padding:0}
html,body{width:1200px;height:1200px;overflow:hidden;background:#fff}
body{position:relative;font-family:Inter,sans-serif;color:var(--ink)}
.screen{position:absolute;width:144px;height:302px;background:var(--bg);border-radius:22px;overflow:hidden;border:1px solid #d3d6dd;font-size:5px}
.status{height:16px;display:flex;justify-content:space-between;align-items:center;padding:2px 12px 0;font-size:5px;font-weight:600}
.bar{height:18px;display:flex;align-items:center;justify-content:space-between;padding:0 8px;position:relative}
.bar .title{position:absolute;left:0;right:0;text-align:center;font-size:7px;font-weight:500;pointer-events:none}
.dots{color:#8a909b;font-size:7px;letter-spacing:.5px}
.save{color:var(--teal);font-size:5px;font-weight:600;margin-left:auto;margin-right:6px}
.content{padding:2px 4px}
.tabs{position:absolute;bottom:0;left:0;right:0;height:32px;background:#fff;border-top:1px solid var(--line);display:flex;padding-top:5px}
.tab{flex:1;text-align:center;color:var(--tabgray);font-size:4.2px;position:relative;white-space:nowrap}
.tab i{display:block;width:6px;height:6px;margin:0 auto 2px;background:currentColor;border-radius:2px}
.tab.on{color:var(--blue)}
.tab.on::after{content:"";position:absolute;left:50%;top:17px;width:2px;height:2px;margin-left:-1px;border-radius:50%;background:var(--blue)}
.home{position:absolute;bottom:3px;left:50%;width:46px;height:2px;margin-left:-23px;border-radius:2px;background:#8c919a}
.search{background:#fff;border:1px solid var(--line);border-radius:3px;height:14px;display:flex;align-items:center;padding:0 5px;color:var(--muted);gap:4px;margin-bottom:3px}
.search .adv{margin-left:auto;color:var(--cyan);font-size:4.4px}
.person{background:#fff;border-radius:3px;display:flex;align-items:center;gap:5px;padding:0 5px;height:33px;margin-bottom:3px}
.avatar{width:15px;height:15px;border-radius:50%;background:linear-gradient(160deg,#d9d4cf,#8e857c);flex:none}
.pname{font-size:5.2px;margin-bottom:3px}
.tags{font-size:4.3px;color:#444;white-space:nowrap}
.tags .o{color:var(--cyan)} .tags .q{color:var(--teal)} .tags .s{color:#c3c7cf;margin:0 1px}
.row{background:#fff;border-radius:3px;display:flex;align-items:center;gap:5px;padding:0 5px;height:22px;margin-bottom:3px;font-size:4.8px}
.prow{background:#fff;border-radius:2px;display:flex;align-items:center;gap:5px;padding:0 5px;height:22px;margin-bottom:3px;font-size:4.8px;white-space:nowrap}
.prow .avatar{width:12px;height:12px}
.plus{width:7px;height:7px;border-radius:1.5px;background:var(--plus);color:#fff;font-size:6px;line-height:7px;text-align:center;font-weight:700;flex:none}
.plus.out{background:none;border:.6px solid #8d939d;color:#8d939d;line-height:6px;font-size:5px}
.field{position:relative;border:.8px solid var(--cyan);border-radius:2px;height:19px;margin:8px 8px 0;padding:7px 6px 0;color:#a4aab4;font-size:4.3px;white-space:nowrap}
.field .lb{position:absolute;top:-4px;left:6px;background:var(--bg);padding:0 2px;color:var(--cyan);font-style:italic;font-weight:500;font-size:5.2px}
.field .caret{position:absolute;right:7px;top:7px;border:3px solid transparent;border-top:3px solid #7a808a}
.trio{display:flex;gap:4px;margin:0 8px}
.trio .field{margin:8px 0 0;flex:1;padding:7px 3px 0;overflow:visible}
.trio .field .lb{left:3px}
.acc{border-radius:3px;padding:6px 7px;margin-bottom:5px;border-left:2.5px solid;font-size:4.4px}
.acc .hd{display:flex;justify-content:space-between;font-weight:600;margin-bottom:6px;font-size:4.6px}
.acc .hd span:last-child{font-weight:400;color:var(--muted)}
.acc .tx{color:#8c929c;line-height:1.35;display:flex;justify-content:space-between;gap:6px}
.acc .add{display:flex;align-items:center;gap:5px;margin-top:8px;border-top:.6px solid rgba(0,0,0,.08);padding-top:6px;color:#555}
.acc.y{background:var(--yellow);border-color:var(--yellowbar)}
.acc.b{background:var(--sky);border-color:var(--skybar)}
.acc.g{background:var(--mint);border-color:var(--mintbar)}
.card{background:#fff;border-radius:3px;padding:5px 6px;margin-bottom:5px}
.flab{color:var(--blue);font-weight:500;font-size:5px;display:flex;justify-content:space-between;margin-top:4px}
.flab:first-child{margin-top:0}
.fval{border:.7px solid #d5d9e0;border-radius:2px;height:10px;padding:2px 4px;color:#979da7;font-size:4.3px;margin-top:3px;white-space:nowrap;overflow:hidden}
.addr{color:#8c929c;font-size:4.3px;line-height:1.35;padding:3px 0 5px;border-bottom:.6px solid var(--line);display:flex;justify-content:space-between;gap:6px}
.addr+.addr{padding-top:6px}
.addline{display:flex;align-items:center;gap:5px;font-size:4.6px;padding-top:6px}
.toolbar{margin:2px 3px 6px;border:.8px solid var(--cyan);border-radius:3px;background:#fff;display:flex;justify-content:space-around;padding:5px 0 4px}
.tool{text-align:center;font-size:4.4px}
.tool i{display:block;width:6px;height:6px;margin:0 auto 4px;background:var(--blue);border-radius:1.5px}
.menu{padding:3px 8px}
.mi{display:flex;align-items:center;gap:7px;height:22.5px;border-bottom:.6px solid var(--line);font-size:5px}
.mi i{width:8px;height:8px;border-radius:2px;background:var(--blue);flex:none}
.seg{display:flex;gap:3px;padding:6px 10px}
.seg span{border:.7px solid #c9cdd4;border-radius:2px;padding:3px 4px;font-size:5px;color:#555;background:#fff;white-space:nowrap}
.seg span.on{background:var(--mint);border-color:var(--teal);color:#1d7c6d}
.cap{position:absolute;width:200px;text-align:center;font-family:Outfit,sans-serif;font-weight:600;font-size:24px;color:#111}
</style>
</head>
<body>

<section class="screen" style="left:62px;top:29px">
  <div class="status"><span>09:46</span><span>▪▪ ▬</span></div>
  <div class="bar"><span></span><span class="title">Contacts</span><span class="dots">···</span></div>
  <div class="content">
    <div class="search"><span>○</span><span>Search</span><span class="adv">Advance Search</span></div>
    <div class="person"><div class="avatar" role="img" aria-label="Contact profile photo"></div><div><div class="pname">Ardell, Corin</div><div class="tags"><span class="o">Aircraft Owner</span><span class="s">|</span>Enthusiast-e<span class="s">|</span>Flight Support</div></div></div>
    <div class="person"><div class="avatar" role="img" aria-label="Contact profile photo"></div><div><div class="pname">Alder, Chase, Bryn</div><div class="tags"><span class="o">Aircraft Owner</span><span class="s">|</span>Pilot<span class="s">|</span><span class="q">Qualified Pilot</span></div></div></div>
    <div class="person"><div class="avatar" role="img" aria-label="Contact profile photo"></div><div><div class="pname">Bellamy, Rowan</div><div class="tags"><span class="o">Aircraft Owner</span><span class="s">|</span>Pilot<span class="s">|</span><span class="q">Qualified Pilot</span></div></div></div>
    <div class="person"><div class="avatar" role="img" aria-label="Contact profile photo"></div><div><div class="pname">Ardell, Corin</div><div class="tags"><span class="o">Aircraft Owner</span><span class="s">|</span>Pilot<span class="s">|</span><span class="q">Qualified Pilot</span></div></div></div>
    <div class="person"><div class="avatar" role="img" aria-label="Contact profile photo"></div><div><div class="pname">Carlo, Ada, Sienna</div><div class="tags">Pilot</div></div></div>
    <div class="person"><div class="avatar" role="img" aria-label="Contact profile photo"></div><div><div class="pname">Ardell, Corin</div><div class="tags">Pilot</div></div></div>
  </div>
  <nav class="tabs"><div class="tab on"><i></i>Contact</div><div class="tab"><i></i>Pilot</div><div class="tab"><i></i>Plane</div><div class="tab"><i></i>Flt Request</div><div class="tab"><i></i>More</div></nav>
  <div class="home"></div>
</section>
<div class="cap" style="left:34px;top:347px">Screen 1</div>

<section class="screen" style="left:296px;top:29px">
  <div class="status"><span>09:46</span><span>▪▪ ▬</span></div>
  <div class="bar"><span>←</span><span class="title">Add Contact</span><span class="save">Save</span><span class="dots">···</span></div>
  <div class="field"><span class="lb">Business Name-e</span>enter your business name</div>
  <div class="field"><span class="lb">First Name-e</span>enter your first name</div>
  <div class="field"><span class="lb">Middle Name-e</span>enter your middle name</div>
  <div class="field"><span class="lb">Last Name-e</span>enter your last name</div>
  <div class="field"><span class="lb">AddressLabelTag -e</span>Select your address type<span class="caret"></span></div>
  <div class="field"><span class="lb">AddressLine1 -e</span>enter your addressline1</div>
  <div class="field"><span class="lb">AddressLine2 -e</span>enter your addressline2</div>
  <div class="trio">
    <div class="field"><span class="lb">City</span>Enter City</div>
    <div class="field"><span class="lb">State</span>Select state</div>
    <div class="field"><span class="lb">Zip -e</span>EnterZipcode</div>
  </div>
  <nav class="tabs"><div class="tab on"><i></i>Contact</div><div class="tab"><i></i>Pilot</div><div class="tab"><i></i>Work Order</div><div class="tab"><i></i>Invoice</div><div class="tab"><i></i>More</div></nav>
  <div class="home"></div>
</section>
<div class="cap" style="left:268px;top:347px">Screen 2</div>

<section class="screen" style="left:515px;top:29px">
  <div class="status"><span>09:46</span><span>▪▪ ▬</span></div>
  <div class="bar"><span>←</span><span class="title">Contact</span><span class="dots">···</span></div>
  <div class="content">
    <div class="row" style="height:25px"><span class="plus">+</span>Add Email -e</div>
    <div class="row" style="height:25px"><span class="plus">+</span>Add Social Media -e</div>
    <div class="row" style="height:25px"><span class="plus">+</span>Add Emergency Contact -e</div>
    <div class="row" style="height:25px"><span class="plus">+</span>Add Personal Information -e</div>
    <div class="row" style="height:25px"><span class="plus">+</span>Add Work Info -e</div>
    <div class="row" style="height:25px"><span class="plus">+</span>Add Skills / Talents -e</div>
    <div class="row" style="height:25px"><span class="plus">+</span>Add Resources -e</div>
    <div class="acc y"><div class="hd"><span>Pilot -e</span><span>Collapse</span></div><div class="tx"><span>Ardell, Corin, 3647946, 10/31/23</span><span>⌄</span></div></div>
  </div>
  <nav class="tabs"><div class="tab on"><i></i>Contact</div><div class="tab"><i></i>Pilot</div><div class="tab"><i></i>Plane</div><div class="tab"><i></i>Flt Request</div><div class="tab"><i></i>More</div></nav>
  <div class="home"></div>
</section>
<div class="cap" style="left:487px;top:347px">Screen 3</div>

<section class="screen" style="left:737px;top:33px">
  <div class="status"><span>09:46</span><span>▪▪ ▬</span></div>
  <div class="bar"><span>←</span><span class="title">Contact</span><span class="dots">···</span></div>
  <div class="content" style="padding:2px 5px">
    <div class="row" style="height:24px"><span class="plus">+</span>Add Resources -e</div>
    <div class="acc y"><div class="hd"><span>Pilot -e</span><span>Collapse</span></div><div class="tx"><span>Ardell, Corin, 3647946, 10/31/23</span><span>⌄</span></div></div>
    <div class="acc b"><div class="hd"><span>Aircraft Owner -e</span><span>Collapse</span></div><div class="tx"><span>Personal : Ardell, Corin: Aerowind: AW-40: Aerowind Aircraft Company, Single Engine, 1100</span><span>⌄</span></div><div class="add"><span class="plus out">+</span>Add Aircraft Owner -e</div></div>
    <div class="acc g"><div class="hd"><span>Qualified Pilot -e</span><span>Collapse</span></div><div class="tx"><span>Personal : Ardell, Corin: Aerowind: AW-40: Aerowind Aircraft Company, Single Engine, 1100</span><span>⌄</span></div><div class="add"><span class="plus out">+</span>Add Qualified Pilot -e</div></div>
  </div>
  <nav class="tabs"><div class="tab on"><i></i>Contact</div><div class="tab"><i></i>Pilot</div><div class="tab"><i></i>Plane</div><div class="tab"><i></i>Flt Request</div><div class="tab"><i></i>More</div></nav>
  <div class="home"></div>
</section>
<div class="cap" style="left:709px;top:347px">Screen 4</div>

<section class="screen" style="left:959px;top:33px">
  <div class="status"><span>09:46</span><span>▪▪ ▬</span></div>
  <div class="bar"><span></span><span class="title">Pilots</span><span class="dots">···</span></div>
  <div class="content">
    <div class="search" style="margin-bottom:5px"><span>○</span><span>Search</span><span class="adv">Advance Search</span></div>
    <div class="prow"><div class="avatar" role="img" aria-label="Pilot profile photo"></div>Alder, Chase, Bryn, 3192133, 9/30/24</div>
    <div class="prow"><div class="avatar" role="img" aria-label="Pilot profile photo"></div>Bellamy, Rowan, 4467155, 2/28/25</div>
    <div class="prow"><div class="avatar" role="img" aria-label="Pilot profile photo"></div>Brenholt, Arlo, 2663187, 10/30/24, 16</div>
    <div class="prow"><div class="avatar" role="img" aria-label="Pilot profile photo"></div>Carlo, Ada, Sienna, 4360575, 3/30/25</div>
    <div class="prow"><div class="avatar" role="img" aria-label="Pilot profile photo"></div>Cano Galvez, Hugo, Yareth</div>
    <div class="prow"><div class="avatar" role="img" aria-label="Pilot profile photo"></div>Garvin, Cole, 3423819, 2/28/25</div>
    <div class="prow"><div class="avatar" role="img" aria-label="Pilot profile photo"></div>Gale, Jasper, Alan, 276135, 3/6/23</div>
    <div class="prow"><div class="avatar" role="img" aria-label="Pilot profile photo"></div>Gale, Jasper, Alan, 276135, 3/6/23</div>
  </div>
  <nav class="tabs"><div class="tab"><i></i>Contact</div><div class="tab on"><i></i>Pilot</div><div class="tab"><i></i>Plane</div><div class="tab"><i></i>Flt Request</div><div class="tab"><i></i>More</div></nav>
  <div class="home"></div>
</section>
<div class="cap" style="left:931px;top:347px">Screen 5</div>

<section class="screen" style="left:62px;top:417px">
  <div class="status"><span>09:46</span><span>▪▪ ▬</span></div>
  <div class="bar"><span>←</span><span class="title">Pilot</span><span class="dots">···</span></div>
  <div class="content" style="padding:2px 6px">
    <div class="card">
      <div class="flab"><span>Pilot -e</span><span class="dots" style="font-size:5px">···</span></div><div class="fval">Alder, Chase, Bryn</div>
      <div class="flab">Pilot Certificate No -e</div><div class="fval">3192133</div>
      <div class="flab">Medical Expiration Date -e</div><div class="fval">9/30/24</div>
      <div class="flab">Flight Review Expiration Date -e</div><div class="fval">6/30/24</div>
      <div class="flab">Total Flight Time -e</div><div class="fval">2500</div>
    </div>
    <div class="card">
      <div class="addr"><span>X99, Pine Reef Airport, Pine Reef, FL, 32699, 11, 2500</span><span>⌄</span></div>
      <div class="addr"><span>C99, Ridgeview Municipal Airport, Ridgeview, CO, 80399, 5,334 ft, 4,800 ft</span></div>
      <div class="addline"><span class="plus">+</span>Add Base Airport -e</div>
    </div>
  </div>
  <nav class="tabs"><div class="tab"><i></i>Contact</div><div class="tab on"><i></i>Pilot</div><div class="tab"><i></i>Plane</div><div class="tab"><i></i>Flt Request</div><div class="tab"><i></i>More</div></nav>
  <div class="home"></div>
</section>
<div class="cap" style="left:34px;top:734px">Screen 6</div>

<section class="screen" style="left:289px;top:414px">
  <div class="status"><span></span><span></span></div>
  <div class="bar"><span>←</span><span class="title">Pilot</span><span class="dots">···</span></div>
  <div class="content" style="padding:2px 6px">
    <div class="card">
      <div class="addr"><span>X99, Pine Reef Airport, Pine Reef, FL, 32699, 11, 2500</span><span>⌄</span></div>
      <div class="addr"><span>C99, Ridgeview Municipal Airport, Ridgeview, CO, 80399, 5,334 ft, 4,800 ft</span></div>
      <div class="addline"><span class="plus">+</span>Add Base Airport -e</div>
    </div>
    <div class="row" style="height:24px"><span class="plus">+</span>Add Ratings -e</div>
    <div class="card">
      <div class="flab"><span>Contact -e</span><span class="dots" style="font-size:5px">···</span></div><div class="fval">Robin Alder</div>
      <div class="flab">Phone -e</div><div class="fval">555-010-7404</div>
      <div class="flab">xxxxxxxx</div><div class="fval">xxxxxxxxxxxx</div>
      <div class="flab">xxxxxxx</div><div class="fval">xxxxxxxxxxxxxx</div>
    </div>
  </div>
  <nav class="tabs"><div class="tab"><i></i>Contact</div><div class="tab on"><i></i>Pilot</div><div class="tab"><i></i>Plane</div><div class="tab"><i></i>Flt Request</div><div class="tab"><i></i>More</div></nav>
  <div class="home"></div>
</section>
<div class="cap" style="left:261px;top:734px">Screen 6.1</div>

<section class="screen" style="left:514px;top:410px">
  <div class="status"><span></span><span></span></div>
  <div class="bar"><span>←</span><span class="title">Work Order</span><span class="dots">···</span></div>
  <div class="toolbar"><div class="tool"><i></i>Print</div><div class="tool"><i></i>Create</div><div class="tool"><i></i>Create</div></div>
  <div class="content" style="padding:0 6px">
    <div class="card">
      <div class="flab"><span>Customer -e</span><span class="dots" style="font-size:5px">···</span></div><div class="fval">Amir, Anwar</div>
      <div class="flab">Service Location -e</div><div class="fval">Billing, 410 Harbor Lane, Austin: TX 78799</div>
      <div class="flab">Billing Address -e</div><div class="fval">Billing, 410 Harbor Lane, Austin: TX 78799</div>
      <div class="flab">Description -e</div><div class="fval">Pool maintenance</div>
      <div class="flab">Work Order Type -e</div><div class="fval">One off job -e</div>
      <div class="flab">Wo Status -e</div><div class="fval">Active -e</div>
      <div class="flab">Billing Frequency -e</div><div class="fval">Upon job completion -e</div>
    </div>
  </div>
  <nav class="tabs"><div class="tab"><i></i>Contact</div><div class="tab"><i></i>Pilot</div><div class="tab on"><i></i>Work Order</div><div class="tab"><i></i>Invoice</div><div class="tab"><i></i>More</div></nav>
  <div class="home"></div>
</section>
<div class="cap" style="left:486px;top:734px">Screen 7</div>

<section class="screen" style="left:736px;top:414px">
  <div class="status"><span>09:46</span><span>▪▪ ▬</span></div>
  <div class="bar"><span>←</span><span class="title">Work Order</span><span class="dots">···</span></div>
  <div class="toolbar"><div class="tool"><i></i>Print</div><div class="tool"><i></i>Create</div><div class="tool"><i></i>Create</div></div>
  <div class="content" style="padding:0 5px">
    <div class="row" style="height:24px"><span class="plus">+</span>Add Email -e</div>
    <div class="row" style="height:24px"><span class="plus">+</span>Add Social Media -e</div>
  </div>
  <nav class="tabs"><div class="tab"><i></i>Contact</div><div class="tab"><i></i>Pilot</div><div class="tab on"><i></i>Work Order</div><div class="tab"><i></i>Invoice</div><div class="tab"><i></i>More</div></nav>
  <div class="home"></div>
</section>
<div class="cap" style="left:708px;top:734px">Screen 7.1</div>

<section class="screen" style="left:960px;top:410px">
  <div class="status"><span>09:46</span><span>▪▪ ▬</span></div>
  <div class="bar"><span>←</span><span class="title">More</span><span class="dots">···</span></div>
  <div class="menu">
    <div class="mi"><i></i>Flight</div>
    <div class="mi"><i></i>Login</div>
    <div class="mi"><i></i>Account</div>
    <div class="mi"><i></i>Calendar</div>
    <div class="mi"><i></i>Users</div>
    <div class="mi"><i></i>Dashboard</div>
    <div class="mi"><i></i>Tracking</div>
    <div class="mi"><i></i>Outreach Event</div>
    <div class="mi"><i></i>Maintenance Resource</div>
    <div class="mi"><i></i>Setting</div>
  </div>
  <nav class="tabs"><div class="tab"><i></i>Contact</div><div class="tab"><i></i>Pilot</div><div class="tab"><i></i>Plane</div><div class="tab"><i></i>Flt Request</div><div class="tab on"><i></i>More</div></nav>
  <div class="home"></div>
</section>
<div class="cap" style="left:932px;top:734px">Screen 8</div>

<section class="screen" style="left:47px;top:829px;width:144px;height:306px">
  <div class="status"><span>09:46</span><span>▪▪ ▬</span></div>
  <div class="bar"><span>←</span><span class="dots">···</span></div>
  <div class="seg"><span>Extra Soft</span><span>Soft</span><span class="on">Medium</span><span style="flex:1;text-align:center">Hard</span></div>
  <div class="home"></div>
</section>
<div class="cap" style="left:14px;top:1147px">Frame 9</div>

</body>
</html>
```